Webdesign für ambulanter Pflegedienst
Zielgruppe
Es ist ein ambulanter Pflegedienst, der sich im Raum Auental um die Versorgung sowie Betreuung von Menschen kümmert. Kontaktdaten: ambulanter Pflegedienst Hand Sorge; Inhaberin: Sabine Lohmar; Birkenweg 14, 06871 Dessau-Roßlau Telefon: 034907/519364
IK-Nummer: 47 283 6194
e-mail: sl-hand-sorge@postfeld.de
Aufgabenstellung
Die Farben sollen in Anlehnung an das Logo sein, dass mit übersandt wird.

```html
<!DOCTYPE html>
<html lang="de">
<head>
<meta charset="utf-8">
<title>Unsere Leistungen – Hand Sorge</title>
<link href="https://fonts.googleapis.com/css2?family=Raleway:wght@400;500;600;700&family=Schoolbell&display=swap" rel="stylesheet">
<style>
:root{
  --teal:#48aaa5;
  --teal-soft:#b2dbd7;
  --sky:#dcedf7;
  --green:#6fa630;
  --text:#5c5c5c;
  --text-soft:#777;
  --white:#fff;
}
*{box-sizing:border-box;margin:0;padding:0}
html,body{width:1200px;height:2346px;overflow:hidden;background:var(--white)}
body{position:relative;font-family:"Raleway",sans-serif;color:var(--text)}
.script{font-family:"Schoolbell",cursive}
.abs{position:absolute}

/* header */
.site-header{left:0;top:0;width:1200px;height:50px;background:var(--white)}
.brand{left:262px;top:18px;display:flex;align-items:center;gap:5px;font-size:10px;font-weight:600;color:var(--teal)}
.brand-dot{width:12px;height:12px;border-radius:50%;background:var(--teal)}
.main-nav{left:418px;top:16px;display:flex;gap:31px;font-size:13px;color:var(--text-soft)}
.main-nav .active{color:var(--green);font-weight:600}
.breadcrumb{left:0;top:50px;width:1200px;height:26px;background:var(--sky);text-align:center;font-size:11px;line-height:26px;color:var(--text)}
.breadcrumb b{color:var(--teal);font-weight:500}
.breadcrumb .script{font-size:11px}

/* hero */
.hero{left:0;top:76px;width:1200px;height:181px;background:linear-gradient(90deg,var(--teal-soft) 0%,#cfe6e2 35%,#e8eee6 55%,#ece9e2 58%)}
.hero-photo{left:665px;top:76px;width:535px;height:181px;background:linear-gradient(90deg,#e9e6df 0%,#d9cbb9 35%,#b9a88f 65%,#c9b7a3 100%)}
.hero-kicker{left:263px;top:130px;font-size:16px;color:var(--text)}
.hero-title{left:262px;top:153px;font-size:33px;font-weight:700;color:var(--text)}
.hero-badge{left:715px;top:163px;width:142px;height:142px;border-radius:50%;background:var(--white);box-shadow:0 4px 10px rgba(0,0,0,.12);display:flex;align-items:center;justify-content:center}

/* accordion */
.accordion-item{left:263px;width:674px;background:var(--white);border:1px solid #e6e6e6;border-radius:5px;box-shadow:0 1px 5px rgba(0,0,0,.08)}
.accordion-head{height:58px;display:flex;align-items:center;justify-content:space-between;padding:0 22px 0 30px;font-size:19px;font-weight:600;color:var(--text)}
.toggle{display:block;width:16px;height:16px}
.accordion-body{padding:0 30px;font-size:12.3px;line-height:15.6px;color:var(--text-soft)}
.accordion-body p{margin-top:3px}
.fristen{position:absolute;left:33px;top:178px;width:608px;height:272px;border:1px solid #bdbdbd;border-top:none;font-size:12.3px;color:var(--text-soft)}
.fristen-head{height:53px;background:var(--sky);font-weight:600;color:var(--text);line-height:15px}
.fristen span{position:absolute}
.closing{position:absolute;left:30px;top:474px;width:610px}

/* contact */
.contact-card{left:330px;top:1430px;width:524px;height:499px;background:var(--white);border-radius:5px;box-shadow:0 2px 10px rgba(0,0,0,.1);overflow:hidden}
.contact-head{height:56px;background:var(--sky);text-align:center;line-height:56px;font-size:16px;color:var(--text)}
.field-label{font-size:12.3px;color:var(--text)}
.field{border:1px solid #c9c9c9;border-radius:6px;background:var(--white)}
.consent{left:83px;top:371px;width:400px;font-size:9.5px;line-height:13.5px;color:var(--text-soft)}
.consent a{color:var(--teal);text-decoration:none}
.submit{left:346px;top:430px;width:153px;height:45px;border-radius:23px;background:var(--teal);color:var(--white);font-size:12px;font-weight:700;text-align:center;line-height:45px;box-shadow:0 3px 6px rgba(0,0,0,.15)}

/* footer */
.footer-band{left:0;top:2062px;width:1200px;height:237px;background:linear-gradient(90deg,var(--teal-soft) 0%,#d6e8e3 35%,#eceee6 55%)}
.footer-photo{left:690px;top:2062px;width:510px;height:237px;background:linear-gradient(90deg,rgba(236,236,228,0) 0%,#cdb9a1 30%,#a88c70 60%,#8f7a66 100%)}
.footer-title{left:261px;top:2093px;font-size:19px;color:var(--text)}
.footer-address{left:262px;top:2131px;font-size:12.5px;line-height:19px;color:var(--text);font-style:normal}
.footer-brand{left:520px;top:2168px;width:160px;display:flex;flex-direction:column;align-items:center;gap:8px;font-size:17px;font-weight:600;color:var(--teal)}
.footer-brand i{width:36px;height:36px;border-radius:50%;background:var(--teal)}
.to-top{left:832px;top:2003px;width:104px;height:104px;border-radius:50%;background:var(--sky);text-align:center;font-size:13px;color:var(--text)}
.bottom-bar{left:0;top:2299px;width:1200px;height:47px;background:var(--sky);font-size:10px;color:var(--text)}
.bottom-bar span{position:absolute;top:18px;font-weight:700}
.bottom-bar .copyright{font-weight:400;font-size:9px;top:19px}
</style>
</head>
<body>

<header class="site-header abs">
  <div class="brand abs"><i class="brand-dot"></i>HAND SORGE</div>
  <nav class="main-nav abs">
    <span>Startseite</span><span>Sofortige Hilfen</span><span class="active">Unsere Leistungen</span><span>Karriere</span><span>Pflegekurse</span>
  </nav>
</header>
<div class="breadcrumb abs"><b>Hand Sorge</b> - <span class="script">Pflege von Mensch zu Mensch</span></div>

<section class="hero abs"></section>
<div class="hero-photo abs" role="img" aria-label="Foto: lachende Pflegekraft mit älterer Dame in einer Küche"></div>
<div class="hero-kicker abs script">Vollumfänglicher Service für Sie</div>
<h1 class="hero-title abs">Unsere Leistungen</h1>
<div class="hero-badge abs">
  <svg width="60" height="54" viewBox="0 0 60 54" aria-hidden="true"><path d="M30 50 C10 36 3 26 3 16 A12 12 0 0 1 30 10 A12 12 0 0 1 57 16 C57 26 50 36 30 50Z" fill="none" stroke="#555" stroke-width="3"/><path d="M30 40 C20 32 16 27 16 21 A6 6 0 0 1 30 19 A6 6 0 0 1 44 21 C44 27 40 32 30 40Z" fill="#666"/></svg>
</div>

<div class="accordion-item abs" style="top:360px"><div class="accordion-head">Grundpflege<svg class="toggle" viewBox="0 0 16 16"><path d="M6 0h4v6h6v4h-6v6H6v-6H0V6h6z" fill="#48aaa5"/></svg></div></div>
<div class="accordion-item abs" style="top:424px"><div class="accordion-head">Behandlungspflege<svg class="toggle" viewBox="0 0 16 16"><path d="M6 0h4v6h6v4h-6v6H6v-6H0V6h6z" fill="#48aaa5"/></svg></div></div>

<div class="accordion-item abs" style="top:488px;height:568px">
  <div class="accordion-head">Beratungseinsatz nach §37 Abs. 3 SGB XI<svg class="toggle" viewBox="0 0 16 16"><rect x="0" y="8" width="16" height="4" fill="#48aaa5"/></svg></div>
  <div class="accordion-body">
    <p>Für Pflegegeldempfänger ist der Beratungseinsatz nach §37 Abs. 3 SGB XI verpflichtend. Dies bedeutet, dass Pflegebedürftige, die Pflegegeld für die häusliche Pflege beziehen und dabei keinerlei Hilfe von einer professionellen Pflegekraft erhalten, gesetzlich dazu verpflichtet sind, sich regelmäßig beraten zu lassen. Jeder Pflegegeldempfänger kann dabei selbstständig entscheiden von wem er sich beraten lässt. Es kann sowohl eine von der Pflegekasse beauftragte Pflegefachkraft sein als auch ein zugelassener Pflegedienst. Nachstehend sind folgende Fristen für die Beratung gesetzlich verankert und aufgezeigt.</p>
  </div>
  <div class="fristen">
    <div class="fristen-head">
      <span style="left:12px;top:14px">Pflegegeldempfänger<br>je Pflegegrad</span>
      <span style="left:205px;top:14px">Beratungseinsatz nach<br>§37 Abs. 3 SGB XI</span>
      <span style="left:382px;top:14px">Einzuhaltende Fristen<br>der Beratung</span>
    </div>
    <span style="left:12px;top:76px">Pflegegrad 1</span><span style="left:205px;top:78px;line-height:15.5px">Nicht zwangsläufig<br>vorgschrieben, 1 x pro<br>Halbjahr möglich</span><span style="left:382px;top:78px">keine</span>
    <span style="left:12px;top:159px">Pflegegrad 2</span><span style="left:205px;top:159px">1 x pro Halbjahr</span><span style="left:382px;top:159px">30.06., 31.12.</span>
    <span style="left:12px;top:187px">Pflegegrad 3</span><span style="left:205px;top:187px">1x pro Halbjahr</span><span style="left:382px;top:187px">30.06., 31.12.</span>
    <span style="left:12px;top:215px">Pflegegrad 4</span><span style="left:205px;top:215px">1 x pro Vierteljahr</span><span style="left:382px;top:215px">31.03., 30.06., 30.09., 31.12.</span>
    <span style="left:12px;top:243px">Pflegegrad 5</span><span style="left:205px;top:243px">1 x por Vierteljahr</span><span style="left:382px;top:243px">31.03., 30.06., 30.09., 31.12.</span>
  </div>
  <p class="closing accordion-body" style="padding:0">Selbstverständlich übernehmen wir diese Beratung gern für sie. Dabei ist es unser Ziel sie über das Angebot der Pflegekasse sowie der Krankenkassen aufzuklären. Dies beinhaltet die Durchführung von Pflegekursen beziehungsweise Einzelschulungen (gem. § 45 SGB XI) oder weitere Entlastungsmöglichkeiten für pflegende Angehörige.</p>
</div>

<div class="accordion-item abs" style="top:1066px"><div class="accordion-head">Verhinderungspflege nach §39 SGB XII<svg class="toggle" viewBox="0 0 16 16"><path d="M6 0h4v6h6v4h-6v6H6v-6H0V6h6z" fill="#48aaa5"/></svg></div></div>
<div class="accordion-item abs" style="top:1130px"><div class="accordion-head">Entlastungs- und Betreuungsangebote gem. §45b SGB XI<svg class="toggle" viewBox="0 0 16 16"><path d="M6 0h4v6h6v4h-6v6H6v-6H0V6h6z" fill="#48aaa5"/></svg></div></div>
<div class="accordion-item abs" style="top:1194px"><div class="accordion-head">Hauswirtschaftliche Leistungen<svg class="toggle" viewBox="0 0 16 16"><path d="M6 0h4v6h6v4h-6v6H6v-6H0V6h6z" fill="#48aaa5"/></svg></div></div>
<div class="accordion-item abs" style="top:1257px"><div class="accordion-head">Sonstige Leistungen<svg class="toggle" viewBox="0 0 16 16"><path d="M6 0h4v6h6v4h-6v6H6v-6H0V6h6z" fill="#48aaa5"/></svg></div></div>

<form class="contact-card abs">
  <div class="contact-head script">Nehmen Sie Kontakt mit uns auf!</div>
  <label class="field-label abs" style="left:39px;top:87px">Nachname*</label>
  <div class="field abs" style="left:39px;top:109px;width:223px;height:40px"></div>
  <label class="field-label abs" style="left:276px;top:87px">Vorname*</label>
  <div class="field abs" style="left:276px;top:109px;width:223px;height:40px"></div>
  <label class="field-label abs" style="left:39px;top:164px">E-Mail*</label>
  <div class="field abs" style="left:39px;top:185px;width:255px;height:40px"></div>
  <label class="field-label abs" style="left:309px;top:164px">Telefonnummer*</label>
  <div class="field abs" style="left:309px;top:185px;width:190px;height:40px"></div>
  <label class="field-label abs" style="left:39px;top:240px">Ihr Anliegen:</label>
  <div class="field abs" style="left:39px;top:261px;width:460px;height:85px"></div>
  <div class="field abs" style="left:39px;top:365px;width:28px;height:28px;border-radius:4px"></div>
  <p class="consent abs">Sie erklären sich damit einverstanden, dass Ihre Daten zur Bearbeitung Ihres Anliegens verwendet werden. Weitere Informationen und Widerrufshinweise finden Sie in der <a>Datenschutzerklärung</a>.</p>
  <div class="submit abs">Abenden</div>
</form>

<footer>
  <div class="footer-band abs"></div>
  <div class="footer-photo abs" role="img" aria-label="Foto: junge Hände halten die Hände einer älteren Person"></div>
  <div class="footer-title abs script">Wir sind für Sie da!</div>
  <address class="footer-address abs">
    ambulanter Pflegedienst Hand Sorge<br>Inhaberin: Sabine Lohmar<br>Birkenweg 14<br>06871 Auental<br>
    <span style="display:block;margin-top:11px">034907/519364<br>sl-hand-sorge@postfeld.de</span>
  </address>
  <div class="footer-brand abs"><i></i>HAND SORGE</div>
  <div class="to-top abs script">
    <svg width="20" height="34" viewBox="0 0 20 34" style="margin-top:20px;display:block;margin-left:42px" aria-hidden="true"><path d="M10 2 L18 16 H12 V32 H8 V16 H2 Z" fill="#48aaa5"/></svg>
    <div style="margin-top:4px">Nach oben</div>
  </div>
  <div class="bottom-bar abs">
    <span style="left:274px">KARRIERE</span>
    <span style="left:369px">KONTAKT</span>
    <span style="left:470px">DATENSCHUTZ</span>
    <span style="left:596px">IMPRESSUM</span>
    <span class="copyright" style="left:707px">Copyright 2023 © ambulanter Pflegedienst Hand Sorge</span>
  </div>
</footer>

</body>
</html>
```